Harlow Ironworks Business Card

We need a business card design for a new small metal fabrication business in rural NSW, Australia.

The business (Harlow Ironworks) is owner operated by a man with the initials KB - much of the branding comes from this name.

Harlow Ironworks designs, engineers, repairs and manufactures a range of custom, quality metal works including vehicle trays, agricultural machinery impliments, trailers, wood splitters, fire pits, furniture etc.

The brand position focuses on custom work of the highest quality.

Business card design should show quality, attention to detail and stand out among a mass of business cards.

Logos are in the files

The grey color may be changed on the logo if required to stand out more.

There is an image attached of a simple card that is liked because it is clean, clear, simple, masculine and effective. It says 'quality'. As most of the work we do is custom it would be good to have the business card speak to this.

Target Market(s)

Rural and regional based Australians. Primarily adult male 25-60 yrs. Primary production / rural / travelling lifestyle.

Industry/Entity Type

Metal Fabrication

Contact Information for Business Card

The words 'custom quality fabrications' would be great somewhere perhaps on the backside (not on the information side)
Name
title
Phone: 0418 539 746 and (02) 6193 4827
email: info@harlowiw.com.au
www.harlowiw.com.au

address (2 lines)

Requirements
Nice to have
• Background colour should be very navy blue or black.
Should not have
• NO orange and blue combinations.
• Navy is OK

```html
<!DOCTYPE html>
<html lang="en">
<head>
<meta charset="utf-8">
<title>Harlow Ironworks Business Card</title>
<link rel="stylesheet" href="https://fonts.googleapis.com/css2?family=Source+Sans+3:ital,wght@0,400;0,600;0,700;1,400&display=swap">
<style>
  :root {
    --page-navy: #121c30;
    --card-white: #ffffff;
    --brand-green: #6abb45;
    --ink-grey: #9b9b9b;
    --ink-dark: #4a4a4a;
    --rule-grey: #b8b8b8;
    --on-green: #ffffff;
  }
  * { margin: 0; padding: 0; box-sizing: border-box; }
  html, body {
    width: 1200px; height: 987px; overflow: hidden;
    background: var(--page-navy);
    font-family: "Source Sans 3", sans-serif;
  }
  .card {
    position: absolute;
    width: 615px; height: 351px;
    box-shadow: 0 3px 10px rgba(0,0,0,0.45);
  }
  .card--front { left: 293px; top: 130px; background: var(--card-white); }
  .card--back { left: 292px; top: 505px; background: var(--brand-green); }
  .card__frame { position: absolute; inset: 0; width: 615px; height: 351px; }

  .brand {
    position: absolute; left: 0; right: 0;
    display: flex; align-items: center; justify-content: center; gap: 12px;
    font-weight: 700; line-height: 1; text-transform: uppercase;
  }
  .brand__mark { width: 70px; height: 70px; flex: none; }
  .brand__words { display: flex; flex-direction: column; gap: 6px; }
  .brand__line--main { font-size: 46px; letter-spacing: 4px; }
  .brand__line--sub { font-size: 23px; letter-spacing: 8.5px; }
  .card--front .brand { top: 50px; color: var(--ink-grey); }
  .card--front .brand__mark { background: var(--brand-green); }
  .card--back .brand { top: 120px; color: var(--on-green); }
  .card--back .brand__mark { background: var(--on-green); }

  .holder {
    position: absolute; right: 361px; top: 212px; text-align: right;
  }
  .holder__name {
    color: var(--brand-green); font-weight: 600; font-size: 21px; line-height: 25px;
  }
  .holder__title {
    color: var(--ink-grey); font-size: 16px; line-height: 20px;
  }
  .divider {
    position: absolute; left: 276px; top: 184px; width: 1px; height: 118px;
    background: var(--rule-grey);
  }
  .contacts {
    position: absolute; left: 298px; top: 184px; list-style: none;
  }
  .contacts__item {
    display: flex; align-items: center; gap: 8px;
    height: 23.5px; font-size: 16px; color: var(--ink-dark);
  }
  .contacts__icon { width: 14px; height: 14px; fill: var(--brand-green); flex: none; }

  .tagline {
    position: absolute; left: 0; right: 0; top: 222px; text-align: center;
    color: var(--on-green); font-weight: 600; font-size: 15px; letter-spacing: 5px;
    text-transform: uppercase;
  }
  .website {
    position: absolute; left: 0; right: 0; top: 276px; text-align: center;
    color: var(--on-green); font-style: italic; font-size: 16px; letter-spacing: 2.5px;
  }
</style>
</head>
<body>
  <section class="card card--front" aria-label="Business card front">
    <svg class="card__frame" viewBox="0 0 615 351" aria-hidden="true">
      <polygon points="31,15 584,15 600,31 600,320 584,336 31,336 15,320 15,31"
               fill="none" stroke="var(--brand-green)" stroke-width="3.5"/>
    </svg>
    <div class="brand">
      <span class="brand__mark"></span>
      <span class="brand__words">
        <span class="brand__line--main">Harlow</span>
        <span class="brand__line--sub">Ironworks</span>
      </span>
    </div>
    <div class="holder">
      <p class="holder__name">MARK ELLIS</p>
      <p class="holder__title">CEO/Founder</p>
    </div>
    <div class="divider"></div>
    <ul class="contacts">
      <li class="contacts__item">
        <svg class="contacts__icon" viewBox="0 0 24 24" aria-hidden="true"><path d="M6.6 10.8a15.1 15.1 0 0 0 6.6 6.6l2.2-2.2c.3-.3.7-.4 1-.2 1.1.4 2.3.6 3.6.6.6 0 1 .4 1 1V20c0 .6-.4 1-1 1A17 17 0 0 1 3 4c0-.6.4-1 1-1h3.5c.6 0 1 .4 1 1 0 1.3.2 2.5.6 3.6.1.3 0 .7-.2 1z"/></svg>
        <span>0418 539 746</span>
      </li>
      <li class="contacts__item">
        <svg class="contacts__icon" viewBox="0 0 24 24" aria-hidden="true"><path d="M6.6 10.8a15.1 15.1 0 0 0 6.6 6.6l2.2-2.2c.3-.3.7-.4 1-.2 1.1.4 2.3.6 3.6.6.6 0 1 .4 1 1V20c0 .6-.4 1-1 1A17 17 0 0 1 3 4c0-.6.4-1 1-1h3.5c.6 0 1 .4 1 1 0 1.3.2 2.5.6 3.6.1.3 0 .7-.2 1z"/></svg>
        <span>(02) 6193 4827</span>
      </li>
      <li class="contacts__item">
        <svg class="contacts__icon" viewBox="0 0 24 24" aria-hidden="true"><path d="M2 5h20v14H2z"/><path d="M2 6.5l10 7.5 10-7.5V5H2z" fill="#fff" opacity="0.9"/></svg>
        <span>info@harlowiw.com.au</span>
      </li>
      <li class="contacts__item">
        <svg class="contacts__icon" viewBox="0 0 24 24" aria-hidden="true"><path d="M12 2a7 7 0 0 0-7 7c0 5.2 7 13 7 13s7-7.8 7-13a7 7 0 0 0-7-7zm0 9.5A2.5 2.5 0 1 1 12 6.5a2.5 2.5 0 0 1 0 5z"/></svg>
        <span>Unit 3, 27 Foundry Lane</span>
      </li>
      <li class="contacts__item">
        <span class="contacts__icon" aria-hidden="true"></span>
        <span>Yarrabin NSW 2650</span>
      </li>
    </ul>
  </section>

  <section class="card card--back" aria-label="Business card back">
    <svg class="card__frame" viewBox="0 0 615 351" aria-hidden="true">
      <polygon points="31,12 584,12 603,31 603,320 584,339 31,339 12,320 12,31"
               fill="none" stroke="var(--on-green)" stroke-width="3"/>
    </svg>
    <div class="brand">
      <span class="brand__mark"></span>
      <span class="brand__words">
        <span class="brand__line--main">Harlow</span>
        <span class="brand__line--sub">Ironworks</span>
      </span>
    </div>
    <p class="tagline">Custom Quality Fabrications</p>
    <p class="website">www.harlowiw.com.au</p>
  </section>
</body>
</html>
```